Specialized tax accounting firm needs letterhead design

We need a letterhead design for a professional services firm called R. Everett Lund Inc. The firm is essentially a very specialized tax accounting firm - instead of serving the end consumer, we support other public accounting firms in the area of Canadian and U.S. tax advisory and compliance (i.e. they call us on tax issues too complex for the general practitioner. Our byline is "Tax Support Services for Public Accounting Firms". Our letterhead should utilize our logo and be based on colours present in our logo (see file attached). The final design needs to convey professionalism and trustworthiness (we're hired by accountants after all!) while being creative and eye-catching.

I've attached:
The font used in the logo
The logo itself in a variety of file formats
A single page showing the key firm information which should be appearing in the letterhead

Please note that there is much more leather background around the logo than needs to be incorporated in the letterhead.

Industry/Entity Type

Accounting

```html
<!DOCTYPE html>
<html lang="en">
<head>
<meta charset="utf-8">
<title>R. Everett Lund Inc. — Stationery</title>
<link rel="stylesheet" href="https://fonts.googleapis.com/css2?family=Cormorant+Garamond:wght@600&family=Source+Sans+3:wght@400;600&family=Tinos&display=swap">
<style>
:root{
  --backdrop:#dcdcdc;
  --paper:#ffffff;
  --brand-blue:#2581c4;
  --brand-orange:#f7931e;
  --ink:#1d1d1f;
  --body-ink:#4a4a4a;
  --soft-ink:#7a7a7a;
  --field:#e9eaec;
  --serif:"Cormorant Garamond", "Times New Roman", serif;
  --sans:"Source Sans 3", Arial, sans-serif;
  --body-serif:"Tinos", "Times New Roman", serif;
}
*{box-sizing:border-box;margin:0;padding:0}
html,body{width:1200px;height:687px;overflow:hidden;background:var(--backdrop)}
.board{position:relative;width:1200px;height:687px}
.sheet{position:absolute;background:var(--paper);box-shadow:0 2px 6px rgba(0,0,0,.25);overflow:hidden}

/* envelope back */
.envelope-back{left:18px;top:152px;width:385px;height:186px}
.envelope-flap{position:absolute;left:0;top:0;width:100%;height:63px;background:var(--brand-blue);border-radius:0 0 18px 18px;display:flex;align-items:center;justify-content:center}
.flap-name{font-family:var(--serif);font-weight:600;font-size:14px;letter-spacing:.08em;color:var(--paper)}

/* envelope front */
.envelope-front{left:18px;top:376px;width:385px;height:186px}

/* firm name */
.firm-name{position:absolute;font-family:var(--serif);font-weight:600;color:var(--ink);letter-spacing:.06em;line-height:1;white-space:nowrap}
.envelope-front .firm-name{left:19px;top:30px;font-size:20px}
.letterhead .firm-name{left:0;width:100%;text-align:center;top:50px;font-size:21px}

.return-address{position:absolute;left:19px;top:89px;font-family:var(--sans);font-weight:600;font-size:9px;line-height:12px;color:var(--brand-blue)}

/* footer bands */
.band-accent{position:absolute;left:0;width:100%;height:5px;background:var(--brand-orange)}
.band-main{position:absolute;left:0;width:100%;bottom:0;background:var(--brand-blue)}
.envelope-front .band-accent{bottom:38px}
.envelope-front .band-main{height:34px}
.letterhead .band-accent{bottom:35px}
.letterhead .band-main{height:31px}

/* letterheads */
.letterhead{width:356px;height:504px}
.letterhead-plain{left:430px;top:102px}
.letterhead-fax{left:823px;top:104px}

.recipient{position:absolute;left:27px;top:110px;font-family:var(--sans);font-size:6px;line-height:7px;color:var(--body-ink)}
.letter-body{position:absolute;left:27px;width:302px;font-size:5.6px;line-height:7.1px;color:var(--body-ink)}
.letter-body p{margin-bottom:6.5px}
.letter-body .sans{font-family:var(--sans)}
.letter-body .serif{font-family:var(--body-serif);color:var(--soft-ink)}
.letterhead-plain .letter-body{top:148px}
.letterhead-fax .letter-body{top:212px}

.signature{position:absolute;left:27px;width:64px;height:28px;border-radius:4px;background:linear-gradient(90deg,#efefef,#e2e2e2)}
.letterhead-plain .signature{top:372px}
.letterhead-fax .signature{top:380px}

.contacts{position:absolute;font-family:var(--sans);font-size:8.6px;line-height:12px;color:var(--ink);list-style:none}
.contacts li{display:flex;align-items:center;gap:5px}
.contacts svg{width:6px;height:6px;fill:var(--brand-blue);flex:none}
.contacts-phone{left:27px;top:428px}
.contacts-web{left:220px;top:434px}

.footer-address{position:absolute;left:0;width:100%;top:489px;text-align:center;font-family:var(--sans);font-weight:600;font-size:8.6px;color:var(--paper)}

/* fax form */
.fax-form{position:absolute;left:23px;top:100px;width:308px;display:grid;grid-template-columns:40px 108px 40px 111px;column-gap:3px;row-gap:2px;font-family:var(--sans);font-size:5.8px;color:var(--ink)}
.fax-form span{background:var(--field);height:15px;line-height:15px;padding-left:4px}
.fax-form .gap{margin-left:3px}
.fax-flags{position:absolute;left:24px;top:171px;width:300px;display:flex;justify-content:space-between;font-family:var(--sans);font-weight:600;font-size:5.4px;color:var(--ink);list-style:none}
.fax-flags li{display:flex;align-items:center;gap:4px}
.fax-flags li::before{content:"";width:6px;height:6px;border:.7px solid #777;background:var(--paper)}
</style>
</head>
<body>
<main class="board">

  <section class="sheet envelope-back" aria-label="Envelope back">
    <div class="envelope-flap"><span class="flap-name">R. EVERETT LUND INC.</span></div>
  </section>

  <section class="sheet envelope-front" aria-label="Envelope front">
    <span class="firm-name">R. EVERETT LUND INC.</span>
    <p class="return-address">2270 Meridian Way,<br>Fairview, CA 95830</p>
    <div class="band-accent"></div>
    <div class="band-main"></div>
  </section>

  <section class="sheet letterhead letterhead-plain" aria-label="Letterhead">
    <span class="firm-name">R. EVERETT LUND INC.</span>
    <p class="recipient">Lpsum, lorem<br>dolor sit amet<br>Lorem, dummy text</p>
    <div class="letter-body">
      <p class="sans">Lorem ipsum dolor sit amet, consetetur sadipscing elitr, sed diam nonumy eirmod tempor invidunt ut labore et dolore magna aliquyam erat, sed diam voluptua. At vero eos et accusam et justo duo dolores et ea rebum. Stet clita kasd gubergren, no sea takimata sanctus est Lorem ipsum dolor sit</p>
      <p class="sans">Lorem ipsum dolor sit amet, consetetur sadipscing elitr, sed diam nonumy eirmod tempor invidunt ut labore et dolore magna aliquyam erat, sed diam voluptua. At vero eos et accusam et justo duo dolores et ea rebum. Stet clita kasd gubergren, no sea takimata sanctus est Lorem ipsum dolor sit amet. Lorem ipsum dolor sit amet, consetetur sadipscing elitr, sed diam nonumy eirmod tempor invidunt ut labore et dolore magna aliquyam erat, sed diam voluptua. At vero eos et accusam et justo duo dolores et ea rebum. Stet clita kasd gubergren, no sea takimata sanctus est Lorem ipsum dolor sit amet. Lorem ipsum dolor sit amet, consetetur sadipscing elitr, sed diam nonumy eirmod tempor invidunt ut labore et dolore magna aliquyam erat, sed diam voluptua. At vero eos et accusam et justo duo dolores et ea rebum. Stet clita kasd gubergren, no sea takimata sanctus est</p>
      <p class="serif">Duis autem vel eum iriure dolor in hendrerit in vulputate velit esse molestie consequat, vel illum dolore eu feugiat nulla facilisis at vero eros et accumsan et iusto odio dignissim qui blandit praesent luptatum zzril delenit augue duis dolore te feugait nulla facilisi. Lorem ipsum dolor sit amet, consectetuer adipiscing elit, sed diam nonummy nibh euismod tincidunt ut laoreet dolore magna aliquam erat volutpat.</p>
      <p class="serif">Ut wisi enim ad minim veniam, quis nostrud exerci tation ullamcorper suscipit lobortis nisl ut aliquip ex ea commodo consequat. Duis autem vel eum iriure dolor in hendrerit in vulputate velit esse molestie consequat, vel illum dolore eu feugiat nulla facilisis at vero eros et accumsan et iusto odio dignissim qui blandit praesent luptatum zzril delenit augue duis dolore te feugait nulla facilisi.</p>
    </div>
    <div class="signature" role="img" aria-label="Handwritten signature"></div>
    <ul class="contacts contacts-phone">
      <li><svg viewBox="0 0 6 6"><path d="M1 0h1.5l.5 1.6-1 .7a3.5 3.5 0 0 0 1.7 1.7l.7-1L6 3.5V5c0 .6-.4 1-1 1A5 5 0 0 1 0 1c0-.6.4-1 1-1z"/></svg>(555) 214-3890</li>
      <li><svg viewBox="0 0 6 6"><path d="M1.5 0h3v2h-3zM0 2.3h6V6H0z"/></svg>(555) 214-3891</li>
      <li><svg viewBox="0 0 6 6"><path d="M1.5 0h3a.5.5 0 0 1 .5.5v5a.5.5 0 0 1-.5.5h-3a.5.5 0 0 1-.5-.5v-5a.5.5 0 0 1 .5-.5zM1.7.8v3.8h2.6V.8z"/></svg>(555) 608-1742</li>
    </ul>
    <ul class="contacts contacts-web">
      <li><svg viewBox="0 0 6 6"><path d="M0 1h6v4H0z"/></svg>mail@yourdomain.com</li>
      <li><svg viewBox="0 0 6 6"><circle cx="3" cy="3" r="3"/></svg>www.yourdomain.com</li>
    </ul>
    <div class="band-accent"></div>
    <div class="band-main"></div>
    <p class="footer-address">2270 Meridian Way, Fairview, CA 95830</p>
  </section>

  <section class="sheet letterhead letterhead-fax" aria-label="Fax cover letterhead">
    <span class="firm-name">R. EVERETT LUND INC.</span>
    <div class="fax-form">
      <span>To</span><span></span><span class="gap">From</span><span></span>
      <span>FAX</span><span></span><span class="gap">Pages</span><span></span>
      <span>Phone</span><span></span><span class="gap">Date</span><span></span>
      <span>Re</span><span></span><span class="gap">CC</span><span></span>
    </div>
    <ul class="fax-flags">
      <li>Urgent</li><li>For Review</li><li>Please comment</li><li>Please reply</li><li>Please recycle</li>
    </ul>
    <div class="letter-body">
      <p class="sans">Lorem ipsum dolor sit amet, consetetur sadipscing elitr, sed diam nonumy eirmod tempor invidunt ut labore et dolore magna aliquyam erat, sed diam voluptua. At vero eos et accusam et justo duo dolores et ea rebum. Stet clita kasd gubergren, no sea takimata sanctus est Lorem ipsum dolor sit</p>
      <p class="sans">Lorem ipsum dolor sit amet, consetetur sadipscing elitr, sed diam nonumy eirmod tempor invidunt ut labore et dolore magna aliquyam erat, sed diam voluptua. At vero eos et accusam et justo duo dolores et ea rebum. Stet clita kasd gubergren, no sea takimata sanctus est Lorem ipsum dolor sit amet. Lorem ipsum dolor sit amet, consetetur sadipscing elitr, sed diam nonumy eirmod tempor invidunt ut labore et dolore magna aliquyam erat, sed diam voluptua. At vero eos et accusam et justo duo dolores et ea rebum. Stet clita kasd gubergren, no sea takimata sanctus est Lorem ipsum dolor sit amet. Lorem ipsum dolor sit amet, consetetur sadipscing elitr, sed diam nonumy eirmod tempor invidunt ut labore et dolore magna aliquyam erat, sed diam voluptua. At vero eos et accusam et justo duo dolores et ea rebum. Stet clita kasd gubergren, no sea takimata sanctus est</p>
      <p class="serif">Duis autem vel eum iriure dolor in hendrerit in vulputate velit esse molestie consequat, vel illum dolore eu feugiat nulla facilisis at vero eros et accumsan et iusto odio dignissim qui blandit praesent luptatum zzril delenit augue duis dolore te feugait nulla facilisi. Lorem ipsum dolor sit amet, consectetuer adipiscing elit, sed diam nonummy nibh euismod tincidunt ut laoreet dolore magna aliquam erat volutpat.</p>
    </div>
    <div class="signature" role="img" aria-label="Handwritten signature"></div>
    <ul class="contacts contacts-phone">
      <li><svg viewBox="0 0 6 6"><path d="M1 0h1.5l.5 1.6-1 .7a3.5 3.5 0 0 0 1.7 1.7l.7-1L6 3.5V5c0 .6-.4 1-1 1A5 5 0 0 1 0 1c0-.6.4-1 1-1z"/></svg>(555) 214-3890</li>
      <li><svg viewBox="0 0 6 6"><path d="M1.5 0h3v2h-3zM0 2.3h6V6H0z"/></svg>(555) 214-3891</li>
      <li><svg viewBox="0 0 6 6"><path d="M1.5 0h3a.5.5 0 0 1 .5.5v5a.5.5 0 0 1-.5.5h-3a.5.5 0 0 1-.5-.5v-5a.5.5 0 0 1 .5-.5zM1.7.8v3.8h2.6V.8z"/></svg>(555) 608-1742</li>
    </ul>
    <ul class="contacts contacts-web">
      <li><svg viewBox="0 0 6 6"><path d="M0 1h6v4H0z"/></svg>mail@yourdomain.com</li>
      <li><svg viewBox="0 0 6 6"><circle cx="3" cy="3" r="3"/></svg>www.yourdomain.com</li>
    </ul>
    <div class="band-accent"></div>
    <div class="band-main"></div>
    <p class="footer-address">2270 Meridian Way, Fairview, CA 95830</p>
  </section>

</main>
</body>
</html>
```